Bref créative
Dormly Nest
HMO Specialists
Professional
Rafik Toumi
Partner
We dont want an adress on the business card
Rafik@dormlynest.co.uk
www.dormlynest.co.uk
I Would like to try with HMO Specialists...O
Or
Letting Agency
Or nothing in the subtitle
The Logo

```html
<!DOCTYPE html>
<html lang="en">
<head>
<meta charset="utf-8">
<title>Dormly Nest – Business Cards</title>
<link href="https://fonts.googleapis.com/css2?family=Arimo:wght@400;700&display=swap" rel="stylesheet">
<style>
  :root {
    --page-bg: #ecebe8;
    --card-white: #ffffff;
    --blue-deep: #0f4f86;
    --blue-mid: #1f6fae;
    --blue-light: #4aa3db;
    --accent-green: #4f9a2c;
    --brand-blue: #1b4f7d;
    --text-light: #ffffff;
    --text-soft: #dbe9f5;
  }
  * { margin: 0; padding: 0; box-sizing: border-box; }
  html, body { width: 1200px; height: 852px; overflow: hidden; }
  body {
    background: var(--page-bg);
    font-family: "Arimo", Arial, sans-serif;
    position: relative;
  }
  .card {
    position: absolute;
    width: 540px;
    height: 310px;
    border-radius: 22px;
    overflow: hidden;
    background: var(--card-white);
    box-shadow: 0 10px 24px rgba(0,0,0,0.18);
  }
  .card--front { left: 40px; top: 170px; }
  .card--back { left: 620px; top: 372px; }
  .card__art { position: absolute; inset: 0; width: 100%; height: 100%; }
  .holder { position: absolute; top: 26px; color: var(--text-light); }
  .holder__name { font-weight: 700; font-size: 16px; }
  .holder__role { font-size: 12px; color: var(--text-soft); margin-top: 8px; }
  .contacts {
    position: absolute; bottom: 26px; list-style: none;
    color: var(--text-light); font-size: 12.5px; line-height: 20px;
  }
  .contacts li { display: flex; align-items: center; gap: 8px; }
  .contacts svg { width: 12px; height: 12px; fill: var(--text-light); flex: none; }
  .card--front .holder, .card--front .contacts { left: 26px; }
  .card--back .holder, .card--back .contacts { right: 26px; text-align: right; }
  .card--back .contacts li { flex-direction: row-reverse; justify-content: flex-start; }
  .brand {
    position: absolute; top: 50%; transform: translateY(-50%);
    display: flex; align-items: center; gap: 10px;
    white-space: nowrap;
  }
  .card--front .brand { left: 262px; }
  .card--back .brand { left: 40px; }
  .brand__dot { width: 24px; height: 24px; border-radius: 50%; background: var(--brand-blue); flex: none; }
  .brand__name {
    font-weight: 700; font-size: 26px; color: var(--brand-blue);
    letter-spacing: 0.5px; text-transform: uppercase; line-height: 1;
  }
</style>
</head>
<body>
  <svg width="0" height="0" style="position:absolute">
    <defs>
      <radialGradient id="panelGlow" cx="0.45" cy="0.4" r="0.8">
        <stop offset="0" stop-color="#4aa3db"/>
        <stop offset="0.5" stop-color="#1f6fae"/>
        <stop offset="1" stop-color="#0f4f86"/>
      </radialGradient>
      <symbol id="icon-phone" viewBox="0 0 24 24"><path d="M6.6 10.8a15 15 0 0 0 6.6 6.6l2.2-2.2c.3-.3.7-.4 1-.2 1.1.4 2.3.6 3.6.6.6 0 1 .4 1 1V20c0 .6-.4 1-1 1A17 17 0 0 1 3 4c0-.6.4-1 1-1h3.5c.6 0 1 .4 1 1 0 1.300.2 2.5.6 3.6.1.3 0 .7-.2 1z"/></symbol>
      <symbol id="icon-mobile" viewBox="0 0 24 24"><path d="M7 1h10a2 2 0 0 1 2 2v18a2 2 0 0 1-2 2H7a2 2 0 0 1-2-2V3a2 2 0 0 1 2-2zm0 3v14h10V4zm5 15.5a1.2 1.2 0 1 0 0 2.4 1.2 1.2 0 0 0 0-2.4z"/></symbol>
      <symbol id="icon-mail" viewBox="0 0 24 24"><path d="M2 5h20v14H2zm2 2v.5l8 5 8-5V7zm0 2.8V17h16V9.8l-8 5z"/></symbol>
      <symbol id="icon-web" viewBox="0 0 24 24"><path d="M12 2a10 10 0 1 0 0 20 10 10 0 0 0 0-20zm6.9 6h-3a15 15 0 0 0-1.3-3.9A8 8 0 0 1 18.900 8zM12 4c.8 1.2 1.5 2.5 1.9 4h-3.8c.4-1.5 1.1-2.8 1.9-4zM4.3 14a8 8 0 0 1 0-4h3.4a16 16 0 0 0 0 4zm.8 2h3a15 15 0 0 0 1.3 3.9A8 8 0 0 1 5.1 16zm3-8h-3a8 8 0 0 1 4.3-3.9A15 15 0 0 0 8.1 8zM12 20c-.8-1.2-1.5-2.5-1.9-4h3.8c-.4 1.5-1.1 2.8-1.9 4zm2.3-6H9.7a14 14 0 0 1 0-4h4.6a14 14 0 0 1 0 4zm.3 5.9A15 15 0 0 0 15.9 16h3a8 8 0 0 1-4.3 3.9zm1.7-5.9a16 16 0 0 0 0-4h3.4a8 8 0 0 1 0 4z"/></symbol>
    </defs>
  </svg>

  <section class="card card--front" aria-label="Business card, front">
    <svg class="card__art" viewBox="0 0 540 310" preserveAspectRatio="none" aria-hidden="true">
      <path d="M0 0H300C232 42 200 118 214 196C224 256 204 288 190 310H0Z" fill="url(#panelGlow)"/>
      <path d="M300 0C238 42 206 118 220 196C230 256 210 288 196 310" fill="none" stroke="var(--accent-green)" stroke-width="3"/>
    </svg>
    <div class="holder">
      <p class="holder__name">Rafik Toumi</p>
      <p class="holder__role">Partner</p>
    </div>
    <ul class="contacts">
      <li><svg><use href="#icon-phone"/></svg>01632960160</li>
      <li><svg><use href="#icon-mobile"/></svg>07700900200</li>
      <li><svg><use href="#icon-mail"/></svg>Rafik@dormlynest.co.uk</li>
      <li><svg><use href="#icon-web"/></svg>www.dormlynest.co.uk</li>
    </ul>
    <div class="brand"><span class="brand__dot"></span><span class="brand__name">Dormly Nest</span></div>
  </section>

  <section class="card card--back" aria-label="Business card, reverse layout">
    <svg class="card__art" viewBox="0 0 540 310" preserveAspectRatio="none" aria-hidden="true">
      <path d="M540 0H240C308 42 340 118 326 196C316 256 336 288 350 310H540Z" fill="url(#panelGlow)"/>
      <path d="M240 0C302 42 334 118 320 196C310 256 330 288 344 310" fill="none" stroke="var(--accent-green)" stroke-width="3"/>
    </svg>
    <div class="holder">
      <p class="holder__name">Rafik Toumi</p>
      <p class="holder__role">Partner</p>
    </div>
    <ul class="contacts">
      <li><svg><use href="#icon-phone"/></svg>01632960160</li>
      <li><svg><use href="#icon-mobile"/></svg>07700900200</li>
      <li><svg><use href="#icon-mail"/></svg>Rafik@dormlynest.co.uk</li>
      <li><svg><use href="#icon-web"/></svg>www.dormlynest.co.uk</li>
    </ul>
    <div class="brand"><span class="brand__dot"></span><span class="brand__name">Dormly Nest</span></div>
  </section>
</body>
</html>
```